Flyer-Design für Werbeflyer Teamentwicklung/Coaching als pdf
Zielgruppe
ich berate Personen, Teams und Organisationseinheiten, überwiegend im Profitbereich. (Internationale Konzerne). Mein Beratungsspektrum ist Führung, Prozessverbesserungen, Teamentwicklung
Aufgabenstellung
Der Text ist in Anlehnung an meine HP, Teamentwicklung und Coaching und es sollte eine übersichtliche, infomative 1-2 Seiten entstehen, die ich als erste Werbung/Kontaktaufnahme versenden kann. Die Seiten sollen klar einen Überblick über mein "Schaffen" geben, sollen aber auch schon etwas von meiner Arbeitsweise deutlich machen. (Ich begriefe schnell, formuliere klar und arbeite sehr zielorientiert - allerdings auch schnörkellos!) Diese Seiten sollten überwiegend als Anhang an eine Mail fungieren, im Ausnahmefall aber auch versendet werden.
Das Logo, die Farbe, etc. analog zu meiner HP - ich lass mich da aber auch gern beraten, falls sie andere Ideen haben

```html
<!DOCTYPE html>
<html lang="de">
<head>
<meta charset="utf-8">
<title>Teamentwicklung – Brigitte Moller</title>
<link href="https://fonts.googleapis.com/css2?family=Open+Sans:wght@400;600&family=Tinos:wght@700&display=swap" rel="stylesheet">
<style>
  :root {
    --plum: #7a0a57;
    --slate: #636b6a;
    --text: #5f6665;
    --band: #b9c9c5;
    --band-dark: #8fa19d;
    --white: #ffffff;
    --frame: #7f8887;
  }
  * { margin: 0; padding: 0; box-sizing: border-box; }
  html, body { width: 1200px; height: 846px; overflow: hidden; background: var(--white); }
  .flyer {
    position: relative; width: 1200px; height: 846px; overflow: hidden;
    font-family: "Open Sans", Arial, sans-serif; color: var(--text);
  }
  .accent-block { position: absolute; left: 45px; top: 0; width: 110px; height: 228px; background: var(--plum); }
  .photo-pier {
    position: absolute; left: 849px; top: 0; width: 351px; height: 846px;
    background: linear-gradient(180deg, #3f9ee0 0%, #8ec8ec 18%, #cfe6f2 32%, #8fd9d8 36%, #55c3c6 48%, #b9a78f 62%, #9b8a76 80%, #7d6f62 100%);
  }
  .quote-band { position: absolute; left: 0; top: 27px; width: 1200px; height: 115px; background: var(--band); }
  .quote-frame { position: absolute; left: 45px; top: 10px; width: 468px; height: 96px; }
  .quote-text {
    position: absolute; left: 76px; top: 28px;
    font-family: "Tinos", "Times New Roman", serif; font-weight: 700; font-size: 21px;
    color: var(--white); line-height: 1.55;
  }
  .quote-text .line-two { display: block; padding-left: 73px; }
  .quote-mark {
    position: absolute; font-family: "Tinos", "Times New Roman", serif; font-weight: 700;
    font-size: 30px; color: var(--white); line-height: 1;
  }
  .quote-mark.open { left: 38px; top: 20px; }
  .quote-mark.close { left: 502px; top: 74px; }
  .brand-mark {
    position: absolute; left: 1034px; top: 0; width: 123px; height: 115px;
    background: var(--band-dark); display: flex; align-items: center; justify-content: center;
    text-align: center; color: var(--white); font-weight: 600; font-size: 15px; line-height: 1.25;
  }
  .headline { position: absolute; right: 650px; top: 190px; text-align: right; }
  .headline h1 { font-weight: 600; font-size: 35px; color: var(--slate); letter-spacing: 0.3px; line-height: 1.15; }
  .headline .name { font-weight: 600; font-size: 27px; color: var(--slate); letter-spacing: 0.5px; line-height: 1.2; }
  .headline .name span { color: var(--plum); }
  .section-label { position: absolute; left: 46px; top: 292px; font-weight: 600; font-size: 18px; color: var(--slate); }
  .benefits { position: absolute; left: 46px; top: 336px; width: 345px; list-style: none; }
  .benefits li {
    position: relative; padding-left: 26px; font-size: 18.5px; line-height: 22.5px; margin-bottom: 11px;
  }
  .benefits li::before {
    content: ""; position: absolute; left: 0; top: 7px; width: 11px; height: 11px; background: var(--plum);
  }
  .body-copy { position: absolute; left: 432px; top: 336px; width: 345px; font-size: 18.5px; line-height: 22.5px; }
  .intro-box {
    position: absolute; left: 866px; top: 453px; width: 296px; height: 341px;
    border: 6px solid var(--frame); background: rgba(255,255,255,0.6);
  }
  .intro-box .side-title {
    position: absolute; left: 4px; bottom: 0; width: 330px; height: 36px;
    transform: rotate(-90deg); transform-origin: 0 0; top: 330px;
    font-size: 29px; color: var(--plum); letter-spacing: 0.5px; line-height: 36px;
  }
  .intro-box p {
    position: absolute; left: 52px; top: 8px; width: 225px;
    font-size: 18.5px; line-height: 24.5px; color: var(--text);
  }
</style>
</head>
<body>
<main class="flyer">
  <div class="accent-block"></div>
  <div class="photo-pier" role="img" aria-label="Foto: Holzsteg mit weißem Geländer, der unter blauem Himmel ins türkisfarbene Meer führt"></div>

  <section class="quote-band">
    <svg class="quote-frame" viewBox="0 0 468 96" aria-hidden="true">
      <polyline points="60,2 2,2 2,94 60,94" fill="none" stroke="#fff" stroke-width="4"/>
      <polyline points="408,2 466,2 466,80" fill="none" stroke="#fff" stroke-width="4"/>
      <polyline points="408,94 440,94" fill="none" stroke="#fff" stroke-width="4"/>
    </svg>
    <span class="quote-mark open">“</span>
    <blockquote class="quote-text">Zu erkennen was geschieht,<span class="line-two">ist der Beginn der Veränderung.</span></blockquote>
    <span class="quote-mark close">”</span>
    <div class="brand-mark">Brigitte<br>Moller</div>
  </section>

  <header class="headline">
    <h1>TEAMENTWICKLUNG</h1>
    <p class="name">BRIGITTE <span>MOLLER</span></p>
  </header>

  <h2 class="section-label">DAZU GEHÖREN</h2>
  <ul class="benefits">
    <li>Eine sorgfältige Analyse der Situation und Festlegung ge­wünschter Resultate</li>
    <li>Überzeugende und förderliche Methoden, die die Lösungskom­petenzen der Menschenim Team unterstützen</li>
    <li>Klare Führung durch den Wider streit von Teaminteressen zwi­schen Verändern, Bewahren, Harmonie und Konfliktbearbei­tung, klarem Feedback und Ein­tracht im Team</li>
    <li>Tragfähigkeit der Ergebnisse</li>
  </ul>

  <p class="body-copy">Is quiant, sequo tempore peligeni­mus dollest isitiur aut provitat eos magnationsed qui dolore plaborunt as architа doluptatia deri audam essi optatur ratiist abor aut laut ea­tium faccuptae et aut ut es sequam recest qui nem re es seque parchit apictem quid et volorererro enias­perem inimporem quam, il iscipidit officidi omnis culpa sus secabo. Sed et arum illenis simus sus recerrum des ut aut il magni consent. perem inimporem quam, il iscipidit officidi omnis culpa sus secabo. Sed et arum illenis simus sus recerrum des ut aut il magni consent. arum illenis simus sus recerrum des ut aut il magni consent. arum illenis simus sus recerrum des ut aut il magni consent. arum illenis simus sus recerrum des ut aut il magni consent.</p>

  <aside class="intro-box">
    <span class="side-title">TEAMENTWICKLUNG</span>
    <p>Teams sind lebendige Gebilde, die um er­folgreich zu sein, sich immer wieder neu ausrichten und koor­dinieren müssen. Das tun sie in aller Regel ohne fremde Hilfe - aber ab und zu ist es hilfreich, Impulse oder Entwicklungs­förderung von außen bekommen.</p>
  </aside>
</main>
</body>
</html>
```